120ml Jar Label — Masculine Cosmetic Foot Balm for Cracked, Hardworking Heels

We need a print-ready wraparound label for a 120ml jar — a brown/amber glass jar with a black metal screw lid (file photo attached).

--DO NOT PUT A BARCODE ON THE LABEL PLEASE--
**PLEASE READ "PLAN HUDDLE PROJECT BRIEF FINAL.MD" IN ATTACHED FILES IF YOU ARE SUBMITTING A DESIGN.**

The label is 190mm wide × 40mm high.
We need files to be in an .ai format with a 2mm bleed at the end.
Social media handle: @bramblekeepnz (facebook, instagram and tiktok)

Bramble Keep is a New Zealand foot-care brand making practical, no-nonsense products for hardworking men whose jobs wreck their feet. Our flagship product, Ridge Mender Balm, helps fix thick, cracked, hardworking skin.

Brand color scheme and overview is all in the brief file. You may add some brand aligned colors outside of the specified hex codes as you see fit to make a great design. Feel free to remove the "Bramble Keep" text from the logo so Bramble Keep is not doubled up on the front of the label

The tone we want: direct, rugged, and credible — like a workwear brand, not a spa brand. Most cracked-heel products on the market lean soft and feminine; we want to stand apart by looking like a serious fix for a real problem, made in New Zealand.

Full legal requirements for New Zealand cosmetic labelling (ingredients, directions, net contents, origin, etc.) are listed in the attached brief document — these are non-negotiable and must stay legible.

Please see the label attached "Label spacing guide" for this project's rough spacing guide. This label is the same size and sits well on the jar. This label doesn't need to be spaced quite as much as the Verin Label

I want to run the design for a week - I feel 7 days is a good amount of time for designers to see the work, digest the brief and create something remarkable and memorable for Bramble Keep.

Target Market(s)

Working men in New Zealand whose jobs or lifestyle put heavy wear on their feet — tradies, farmers, hospital/shift workers, hunters, and outdoors people. Practical, value-driven buyers rather than luxury skincare shoppers.

Industry/Entity Type

Beauty / Health & Wellness / Cosmetics

Font styles to use
Sans Serif
Other font styles liked:
• Montserrat (bold, headings), Inter (regular, body)

Colors
00AB8E
00BBA5
67D7C9
C6EFE9
E9F9F6
FFC000
F8CF3A
FAE287
FDF2CF
FEFAEE

Requirements
Must have
• All NZ cosmetic labelling requirements from the attached brief (product name, tag line, net contents, ingredients, directions, storage, made in NZ) — legible and complete, not omitted for aesthetics Fits 190mm × 40mm wraparound format for a 120ml brown jar with black lid Uses our existing brand colors: Deep Olive #3C4A34, Bone White #F4EFE6, Terracotta Clay #C1683D, and Warm Grey #4A4540 (exact palette in attached brief) Uses Montserrat (headings) and Inter (body) or close equivalents Incorporates our existing shield-and-wing logo (attached) Brand name and product name clearly readable from a normal shelf/bathroom-cabinet distance
Nice to have
• A style that could extend into a hero/product photo later, similar to the NZ-hills-backdrop look on our website (screenshot attached) — not required for the label itself, just good to keep in mind Original icon work (e.g. a small soak/apply/sock icon set) if it fits the rugged brand feel A design that could work as a small back-label/wraparound split if the front can't fit everything at a readable size
Should not have
• No pastel colors, floral motifs, or delicate script fonts — this should never look like spa/luxury skincare. Don't introduce new brand colors outside the palette provided other than black.

```html
<!DOCTYPE html>
<html lang="en">
<head>
<meta charset="utf-8">
<title>Bramble Keep — Ridge Mender Balm Jar Label</title>
<link href="https://fonts.googleapis.com/css2?family=Oswald:wght@400;500;600;700&family=Nunito+Sans:wght@400;600;700&display=swap" rel="stylesheet">
<style>
  :root{
    --page:#ffffff;
    --frame:#1b1c1a;
    --panel-dark:#1f241d;
    --cream:#f3e9d6;
    --cream-line:#dccaa6;
    --gold:#c4902e;
    --gold-soft:#d9ab55;
    --ink:#1f241d;
    --ink-soft:#3a3a34;
  }
  *{box-sizing:border-box;margin:0;padding:0}
  html,body{width:1200px;height:751px;overflow:hidden;background:var(--page)}
  body{position:relative;font-family:"Nunito Sans",Arial,sans-serif;color:var(--ink)}
  .dim{position:absolute;font-family:"Nunito Sans",Arial,sans-serif;font-size:22px;color:#111;white-space:nowrap}
  .dim-width{left:0;width:1200px;top:200px;text-align:center}
  .dim-height{left:40px;top:375px;transform:translate(-50%,-50%) rotate(-90deg)}

  .label{position:absolute;left:70px;top:245px;width:1060px;height:262px;background:var(--frame)}
  .panel{position:absolute;top:8px;height:248px}
  .panel-cream{background:var(--cream)}
  .panel-cream::after{content:"";position:absolute;inset:6px;border:1px solid var(--cream-line);border-radius:3px;pointer-events:none}
  .panel-left{left:9px;width:298px}
  .panel-right{left:755px;width:296px}
  .fern-strip{position:absolute;top:8px;height:248px;width:30px;background:linear-gradient(180deg,#3b3524,#2c2a20 50%,#3b3524);border-left:1px solid var(--gold);border-right:1px solid var(--gold)}
  .fern-left{left:307px}
  .fern-right{left:725px}
  .panel-front{left:337px;width:388px;background:var(--panel-dark);color:var(--cream);text-align:center}

  .heading{font-family:"Oswald",Arial,sans-serif;font-weight:600;text-transform:uppercase;letter-spacing:.02em}
  .abs{position:absolute}
  .center-x{transform:translateX(-50%);white-space:nowrap}

  /* left panel */
  .why-title{left:148px;top:24px;font-size:9.5px}
  .benefit{position:absolute;top:48px;width:86px;text-align:center;transform:translateX(-50%)}
  .benefit-icon{display:block;width:30px;height:30px;margin:0 auto}
  .benefit-name{font-family:"Oswald",Arial,sans-serif;font-weight:600;font-size:9px;margin-top:6px}
  .benefit-text{font-size:6.3px;line-height:1.45;color:var(--ink-soft);margin-top:1px}
  .benefit-rule{position:absolute;top:60px;width:1px;height:28px;background:var(--ink-soft)}
  .trusted-blokes{left:153px;top:128px;font-size:7.2px}
  .workers{left:90px;top:143px;width:128px;height:28px}
  .trades{left:153px;top:180px;font-size:7.4px}
  .directions{left:24px;top:200px;width:250px;font-size:5.9px;line-height:8px;color:var(--ink-soft);text-align:center}
  .directions b{font-family:"Oswald",Arial,sans-serif;font-weight:600;color:var(--ink);letter-spacing:.03em}

  /* front */
  .brand-mark{left:50%;top:18px;width:62px;height:62px;margin-left:-31px;border-radius:50%;background:var(--cream);opacity:.9}
  .brand-name{left:50%;top:92px;font-size:18px;color:var(--cream);font-weight:700;letter-spacing:.01em}
  .brand-nz{left:50%;top:115px;font-size:9px;color:var(--cream)}
  .brand-nz::before,.brand-nz::after{content:"";position:absolute;top:7px;width:36px;height:1px;background:var(--gold)}
  .brand-nz::before{right:18px}
  .brand-nz::after{left:18px}
  .product-main{left:50%;top:123px;font-size:36px;font-weight:700;color:var(--cream);line-height:1.15}
  .product-sub{left:50%;top:161px;font-size:23px;font-weight:700;color:var(--gold);letter-spacing:.04em;line-height:1.1}
  .ribbon{left:99px;top:190px;width:181px;height:16px;background:var(--cream);color:var(--ink);font-family:"Oswald",Arial,sans-serif;font-weight:500;font-size:9.5px;letter-spacing:.1em;line-height:16px;clip-path:polygon(4px 0,calc(100% - 4px) 0,100% 50%,calc(100% - 4px) 100%,4px 100%,0 50%)}
  .ribbon .dot{color:var(--gold)}
  .front-claim{left:50%;top:210px;font-family:"Oswald",Arial,sans-serif;font-size:9.5px;letter-spacing:.03em;color:var(--cream)}
  .front-fern{left:102px;top:228px;width:26px;height:18px;background:var(--gold);border-radius:2px 12px 2px 12px;opacity:.85}
  .origin-box{left:136px;top:229px;height:16px;padding:0 6px;border:1px solid var(--gold);border-radius:2px;font-family:"Oswald",Arial,sans-serif;font-size:8px;letter-spacing:.06em;line-height:14px;color:var(--cream)}
  .net{left:248px;top:228px;font-family:"Oswald",Arial,sans-serif;font-size:9.5px;color:var(--gold-soft);line-height:18px}
  .net::before,.net::after{content:"";display:inline-block;width:10px;height:1px;background:var(--gold);vertical-align:middle;margin:0 4px}

  /* right panel */
  .ing-title{left:71px;top:22px;font-size:8px}
  .ing-list{left:31px;top:33px;width:104px;font-size:5.8px;line-height:8.4px;color:var(--ink-soft)}
  .divider-v{left:142px;top:22px;width:1px;height:88px;background:var(--gold)}
  .checks{left:162px;top:28px;list-style:none}
  .checks li{display:flex;align-items:center;font-family:"Oswald",Arial,sans-serif;font-size:8.3px;line-height:16px;color:var(--ink)}
  .checks svg{width:11px;height:11px;margin-right:8px;flex:none}
  .rule-dot{left:66px;width:152px;height:1px;background:var(--gold)}
  .rule-dot::after{content:"";position:absolute;left:74px;top:-1.5px;width:3px;height:3px;border-radius:50%;background:var(--gold)}
  .trusted-kiwis{left:142px;top:124px;font-size:10px;text-align:center;line-height:14px}
  .badge-plain{left:68px;top:163px;width:40px;height:40px;border:1px solid var(--ink);background:#e9dcc2}
  .animal{left:135px;top:164px;width:30px;height:26px;background:var(--ink);border-radius:40% 40% 30% 30%}
  .animal-text{left:150px;top:192px;font-size:5.8px;text-align:center;line-height:7px}
  .pao{left:188px;top:164px;width:30px;height:34px}
  .storage{left:24px;top:212px;width:248px;font-size:5.9px;line-height:8px;color:var(--ink-soft);text-align:center}
  .storage b{font-family:"Oswald",Arial,sans-serif;font-weight:600;color:var(--ink);letter-spacing:.03em}
</style>
</head>
<body>
  <div class="dim dim-width">190 mm</div>
  <div class="dim dim-height">40 mm</div>

  <section class="label" aria-label="Ridge Mender Balm wraparound jar label">
    <div class="panel panel-cream panel-left">
      <div class="abs center-x heading why-title">Why it works</div>

      <div class="benefit" style="left:66px">
        <span class="benefit-icon" role="img" aria-label="Foot icon in dark circle" style="border-radius:50%;background:var(--panel-dark)"></span>
        <div class="benefit-name">SOFTEN</div>
        <div class="benefit-text">Deeply nourishes and<br>softens thick, dry skin.</div>
      </div>
      <div class="benefit-rule" style="left:110px"></div>
      <div class="benefit" style="left:147px">
        <span class="benefit-icon" role="img" aria-label="Exfoliation sparkle icon in dark circle" style="border-radius:50%;background:var(--panel-dark)"></span>
        <div class="benefit-name">REMOVE</div>
        <div class="benefit-text">Helps lift away rough,<br>dead skin.</div>
      </div>
      <div class="benefit-rule" style="left:192px"></div>
      <div class="benefit" style="left:229px">
        <svg class="benefit-icon" viewBox="0 0 30 30" aria-hidden="true">
          <circle cx="15" cy="15" r="15" fill="var(--panel-dark)"/>
          <path d="M15 7 L21 9.5 V15 C21 19 18.5 21.5 15 23 C11.5 21.5 9 19 9 15 V9.5 Z" fill="none" stroke="var(--cream)" stroke-width="1.2"/>
          <path d="M15 12 V18 M12 15 H18" stroke="var(--cream)" stroke-width="1.4"/>
        </svg>
        <div class="benefit-name">REPAIR</div>
        <div class="benefit-text">Supports skin barrier<br>repair and protection.</div>
      </div>

      <div class="abs center-x heading trusted-blokes">Trusted by hardworking Kiwi blokes</div>
      <div class="abs workers" role="img" aria-label="Silhouettes of a tradie, tractor, medic, hunter and hiker" style="background:linear-gradient(90deg,var(--ink) 0 14%,transparent 14% 22%,var(--ink) 22% 40%,transparent 40% 48%,var(--ink) 48% 60%,transparent 60% 68%,var(--ink) 68% 80%,transparent 80% 88%,var(--ink) 88% 100%);opacity:.85;border-radius:3px"></div>
      <div class="abs center-x heading trades">Tradies • Farmers • Shift workers • Hunters • Outdoors</div>
      <p class="abs directions"><b>DIRECTIONS:</b> Apply a small amount to clean, dry heels and feet once or twice daily. Massage in until absorbed. For best results apply at night and wear socks. For external use only. Avoid broken skin; discontinue if irritation occurs.</p>
    </div>

    <div class="fern-strip fern-left" role="img" aria-label="Vertical gold and cream fern frond border"></div>

    <div class="panel panel-front">
      <span class="abs brand-mark" aria-hidden="true"></span>
      <div class="abs center-x heading brand-name">Bramble Keep</div>
      <div class="abs center-x heading brand-nz">NZ</div>
      <div class="abs center-x heading product-main">Ridge</div>
      <div class="abs center-x heading product-sub">Mender Balm</div>
      <div class="abs ribbon">SOFTEN <span class="dot">•</span> REMOVE <span class="dot">•</span> RESTORE</div>
      <div class="abs center-x front-claim">FOR THICK, CRACKED, HARDWORKING SKIN</div>
      <div class="abs front-fern" role="img" aria-label="Small gold fern leaf"></div>
      <div class="abs origin-box">MADE IN NEW ZEALAND</div>
      <div class="abs net">120ml</div>
    </div>

    <div class="fern-strip fern-right" role="img" aria-label="Vertical gold and cream fern frond border"></div>

    <div class="panel panel-cream panel-right">
      <div class="abs center-x heading ing-title">Ingredients</div>
      <p class="abs ing-list">Shea Butter, Beef Tallow,<br>Beeswax, Grape Seed Oil,<br>Vegetable Glycerin, Lanolin,<br>Panthenol, Gluconolactone,<br>Sodium Benzoate,<br>Allantoin, Manuka Honey,<br>Vitamin E, Tea Tree Essential Oil,<br>Lemon Myrtle Essential Oil,<br>Rosemary Oleoresin Extract.</p>
      <div class="abs divider-v"></div>
      <ul class="abs checks">
        <li><svg viewBox="0 0 12 12" aria-hidden="true"><circle cx="6" cy="6" r="5.2" fill="none" stroke="var(--gold)" stroke-width=".9"/><path d="M3.4 6.2 5.3 8 9 3.8" fill="none" stroke="var(--gold)" stroke-width="1.1"/></svg>NO PARABENS</li>
        <li><svg viewBox="0 0 12 12" aria-hidden="true"><circle cx="6" cy="6" r="5.2" fill="none" stroke="var(--gold)" stroke-width=".9"/><path d="M3.4 6.2 5.3 8 9 3.8" fill="none" stroke="var(--gold)" stroke-width="1.1"/></svg>NO PHTHALATES</li>
        <li><svg viewBox="0 0 12 12" aria-hidden="true"><circle cx="6" cy="6" r="5.2" fill="none" stroke="var(--gold)" stroke-width=".9"/><path d="M3.4 6.2 5.3 8 9 3.8" fill="none" stroke="var(--gold)" stroke-width="1.1"/></svg>NO MINERAL OIL</li>
        <li><svg viewBox="0 0 12 12" aria-hidden="true"><circle cx="6" cy="6" r="5.2" fill="none" stroke="var(--gold)" stroke-width=".9"/><path d="M3.4 6.2 5.3 8 9 3.8" fill="none" stroke="var(--gold)" stroke-width="1.1"/></svg>NO SYNTHETIC COLOURS</li>
        <li><svg viewBox="0 0 12 12" aria-hidden="true"><circle cx="6" cy="6" r="5.2" fill="none" stroke="var(--gold)" stroke-width=".9"/><path d="M3.4 6.2 5.3 8 9 3.8" fill="none" stroke="var(--gold)" stroke-width="1.1"/></svg>MADE IN NEW ZEALAND</li>
      </ul>
      <div class="abs rule-dot" style="top:117px"></div>
      <div class="abs center-x heading trusted-kiwis">Trusted by<br>hardworking Kiwi's</div>
      <div class="abs rule-dot" style="top:156px"></div>
      <div class="abs badge-plain" aria-hidden="true"></div>
      <div class="abs animal" role="img" aria-label="Rabbit silhouette"></div>
      <div class="abs center-x heading animal-text">NOT TESTED<br>ON ANIMALS</div>
      <svg class="abs pao" viewBox="0 0 30 34" aria-hidden="true">
        <path d="M4 8 L26 1" stroke="var(--ink)" stroke-width="1.3" fill="none"/>
        <path d="M4 14 H26 V30 Q26 32 24 32 H6 Q4 32 4 30 Z" fill="none" stroke="var(--ink)" stroke-width="1.3"/>
        <ellipse cx="15" cy="14" rx="11" ry="2" fill="none" stroke="var(--ink)" stroke-width="1"/>
        <text x="15" y="28" text-anchor="middle" font-family="Oswald, Arial, sans-serif" font-weight="600" font-size="9" fill="var(--ink)">12M</text>
      </svg>
      <p class="abs storage"><b>STORAGE:</b> Store in a cool, dry place below 30°C, out of direct sunlight. Keep lid tightly closed. Keep out of reach of children.</p>
    </div>
  </section>
</body>
</html>
```